Delegate Welcome sign

The Copperfield Lodge hotel in Pine Bush NY is welcoming delegations from many different countries during 2019. We want to make a welcome sign about 16:9 ratio about 4 feet high with raised letters. I have attached a background design that we liked and a template with the wording. As you will see I need help with it.

```html
<!DOCTYPE html>
<html lang="en">
<head>
<meta charset="UTF-8">
<title>Delegate Welcome Sign — The Copperfield Lodge</title>
<link rel="stylesheet" href="https://fonts.googleapis.com/css2?family=Overlock:wght@400;700&family=Rammetto+One&display=swap">
<style>
  :root {
    --page: #ffffff;
    --forest-dark: #2f403c;
    --forest: #3a4d48;
    --leaf: #5e8a7e;
    --panel: #e2f0ec;
    --panel-edge: #c9ddd7;
    --ink: #1f2624;
    --headline-shadow: #9fb8b1;
  }
  html, body {
    margin: 0;
    padding: 0;
    width: 1200px;
    height: 1000px;
    overflow: hidden;
    background: var(--page);
  }
  .canvas {
    position: relative;
    width: 1200px;
    height: 1000px;
  }
  .welcome-sign {
    position: absolute;
    left: 251px;
    top: 299px;
    width: 698px;
    height: 401px;
    overflow: hidden;
  }
  .leaf-pattern {
    position: absolute;
    inset: 0;
    background:
      radial-gradient(ellipse at 15% 20%, rgba(94,138,126,0.55), transparent 40%),
      radial-gradient(ellipse at 50% 95%, rgba(94,138,126,0.5), transparent 40%),
      radial-gradient(ellipse at 90% 30%, rgba(94,138,126,0.5), transparent 40%),
      radial-gradient(ellipse at 85% 90%, rgba(94,138,126,0.45), transparent 38%),
      radial-gradient(ellipse at 10% 85%, rgba(94,138,126,0.45), transparent 38%),
      linear-gradient(135deg, var(--forest) 0%, var(--forest-dark) 100%);
  }
  .message-panel {
    position: absolute;
    left: 124px;
    top: 112px;
    width: 450px;
    height: 179px;
    box-sizing: border-box;
    background: var(--panel);
    border: 3px solid var(--panel-edge);
    box-shadow: 0 0 0 1px var(--forest-dark);
    display: flex;
    align-items: center;
    justify-content: center;
  }
  .message-panel::before {
    content: "";
    position: absolute;
    inset: 3px;
    border: 2px solid var(--ink);
    pointer-events: none;
  }
  .message {
    text-align: center;
    color: var(--ink);
    font-family: "Overlock", sans-serif;
    font-weight: 700;
    font-size: 19px;
    line-height: 20px;
  }
  .message p { margin: 0; }
  .message .headline {
    font-family: "Rammetto One", serif;
    font-weight: 400;
    font-size: 20px;
    line-height: 28px;
    margin: 10px 0 6px;
    color: var(--ink);
    letter-spacing: 0;
    text-shadow: 2px 2px 0 var(--headline-shadow);
    white-space: nowrap;
  }
  .message .hashtag {
    font-size: 13px;
    margin-top: 8px;
  }
</style>
</head>
<body>
  <div class="canvas">
    <section class="welcome-sign">
      <div class="leaf-pattern" role="img" aria-label="Leaf pattern in green tones with the word welcome written in many languages"></div>
      <div class="message-panel">
        <div class="message">
          <p>The Copperfield Lodge Hotel</p>
          <p>Welcomes</p>
          <p class="headline">2019 International Delegates</p>
          <p>To The Hudson Valley</p>
          <p>In New York</p>
          <p class="hashtag">#copperfieldlodgehotel</p>
        </div>
      </div>
    </section>
  </div>
</body>
</html>
```